Crestwave Fitness Studio Retail Tube Design

We require a design for cardboard tubes, like images included, which will be the main packaging for the clothing sold in our fitness studio. Crestwave Fitness Studio is an upscale customer service driven fitness studio that is geared towards improving our clients/members quality of life by marrying cutting edge technology like 3D scanning and metabolic measurement with first class training based on 30+ years of experience in the industry.

The project will require a design which revolves around the tube seamlessly including the lid and its top and must include the company logo, which is included, along with our web address (www.crestwavegymhub.example).

The final design should be a bold, sleek design which stands out so when people see the tube they will either know it’s from our studio or be curious as to want company it’s from. Similar to the impact the Tarvanique bag has that is given to all their customers.

Target Market(s)

Individuals and groups seeking individualize fitness programs which produce results.

Industry/Entity Type

Clothing

Colors

Designer to choose colors to be used in the design.

Requirements
Must have
• Logo and website address

```html
<!DOCTYPE html>
<html lang="en">
<head>
<meta charset="utf-8">
<title>Crestwave Fitness Studio – Retail Tube Wraps</title>
<link rel="stylesheet" href="https://fonts.googleapis.com/css2?family=Josefin+Sans:wght@300;400&family=Titillium+Web:wght@700&display=swap">
<style>
  :root {
    --page-bg: #ffffff;
    --kraft-a: #a98a63;
    --kraft-b: #7a5f44;
    --kraft-c: #95784f;
    --charcoal-a: #5e5e60;
    --charcoal-b: #3c3c3e;
    --charcoal-c: #525254;
    --umber-a: #9c8a7e;
    --umber-b: #6f5c50;
    --umber-c: #8a776b;
    --silver-a: #d4d5d7;
    --silver-b: #b5b6b9;
    --silver-c: #c8c9cb;
    --umber-line: #4e3e34;
    --label-white: #ffffff;
    --label-silver: #d3d4d6;
    --label-kraft: #cfb58f;
    --ink: #1e1e1e;
    --brand-red: #c8102e;
    --url-light: #f0f0f0;
    --url-dark: #5c4a40;
    --url-grey: #8e8f92;
  }
  * { box-sizing: border-box; margin: 0; padding: 0; }
  html, body {
    width: 1200px; height: 752px; overflow: hidden;
    background: var(--page-bg);
  }
  .canvas { position: relative; width: 1200px; height: 752px; }

  .wrap {
    position: absolute; top: 100px; width: 234px; height: 556px;
    overflow: hidden;
  }
  .wrap--kraft    { left: 88px; }
  .wrap--charcoal { left: 343px; }
  .wrap--umber    { left: 609px; }
  .wrap--silver   { left: 877px; }

  .wrap__pattern { position: absolute; inset: 0; }
  .wrap--kraft .wrap__pattern {
    background: linear-gradient(160deg, var(--kraft-a) 0%, var(--kraft-c) 45%, var(--kraft-b) 100%);
  }
  .wrap--charcoal .wrap__pattern {
    background: linear-gradient(160deg, var(--charcoal-a) 0%, var(--charcoal-c) 45%, var(--charcoal-b) 100%);
  }
  .wrap--umber .wrap__pattern {
    background: linear-gradient(160deg, var(--umber-a) 0%, var(--umber-c) 45%, var(--umber-b) 100%);
  }
  .wrap--silver .wrap__pattern {
    background: linear-gradient(160deg, var(--silver-a) 0%, var(--silver-c) 45%, var(--silver-b) 100%);
  }

  .label {
    position: absolute; left: 23px; top: 232px;
    width: 188px; height: 148px;
    display: flex; flex-direction: column; align-items: center; justify-content: center;
    gap: 8px;
    border: 2px solid transparent;
    outline: 1.5px solid var(--ink); outline-offset: -7px;
  }
  .wrap--kraft .label    { background: var(--label-kraft); border-color: var(--label-kraft); outline-color: var(--umber-line); }
  .wrap--charcoal .label { background: var(--label-white); border-color: var(--label-white); outline-color: #8a8a8c; }
  .wrap--umber .label    { background: var(--label-white); border-color: var(--umber-line); outline-color: var(--umber-line); }
  .wrap--silver .label   { background: var(--label-silver); border-color: #8c8d90; outline-color: #ffffff; }

  .label__mark {
    width: 34px; height: 34px; background: var(--brand-red);
  }
  .label__name {
    font-family: "Josefin Sans", sans-serif; font-weight: 300;
    color: var(--ink); text-align: center; line-height: 1;
  }
  .label__name-main { display: block; font-size: 33px; letter-spacing: 0.4px; }
  .label__name-sub  { display: block; font-size: 10.5px; font-weight: 400; letter-spacing: 1.6px; margin-top: 4px; }

  .wrap__url {
    position: absolute; left: 0; right: 0; top: 502px;
    text-align: center;
    font-family: "Titillium Web", sans-serif; font-weight: 700;
    font-size: 14.5px; letter-spacing: -0.1px; white-space: nowrap;
  }
  .wrap--kraft .wrap__url, .wrap--charcoal .wrap__url { color: var(--url-light); }
  .wrap--umber .wrap__url  { color: var(--url-dark); }
  .wrap--silver .wrap__url { color: var(--url-grey); }
</style>
</head>
<body>
<main class="canvas">

  <section class="wrap wrap--kraft">
    <div class="wrap__pattern" role="img" aria-label="Repeating geometric pattern of nested dark brown diamonds on kraft paper"></div>
    <div class="label">
      <span class="label__mark"></span>
      <p class="label__name"><span class="label__name-main">crestwave</span><span class="label__name-sub">FITNESS STUDIO</span></p>
    </div>
    <p class="wrap__url">www.crestwavegymhub.example</p>
  </section>

  <section class="wrap wrap--charcoal">
    <div class="wrap__pattern" role="img" aria-label="Repeating grey line pattern of diamonds and four-petal motifs on charcoal"></div>
    <div class="label">
      <span class="label__mark"></span>
      <p class="label__name"><span class="label__name-main">crestwave</span><span class="label__name-sub">FITNESS STUDIO</span></p>
    </div>
    <p class="wrap__url">www.crestwavegymhub.example</p>
  </section>

  <section class="wrap wrap--umber">
    <div class="wrap__pattern" role="img" aria-label="Repeating geometric pattern of nested umber diamonds on white"></div>
    <div class="label">
      <span class="label__mark"></span>
      <p class="label__name"><span class="label__name-main">crestwave</span><span class="label__name-sub">FITNESS STUDIO</span></p>
    </div>
    <p class="wrap__url">www.crestwavegymhub.example</p>
  </section>

  <section class="wrap wrap--silver">
    <div class="wrap__pattern" role="img" aria-label="Repeating light grey line pattern of diamonds and four-petal motifs on white"></div>
    <div class="label">
      <span class="label__mark"></span>
      <p class="label__name"><span class="label__name-main">crestwave</span><span class="label__name-sub">FITNESS STUDIO</span></p>
    </div>
    <p class="wrap__url">www.crestwavegymhub.example</p>
  </section>

</main>
</body>
</html>
```